LED strip light bag design

We are brivexa lighting, a LED strip manufacturer in China, We need a packaging design for our LED strip light, as the strip market is full of standard package, so we want to make our package special, and use color orange, black and grey

Target Market(s)

USA, Europe

Contact Information for Business Card

Morgan Pidd
Director
Shenzhen Brivexa Lighting Co., Ltd.
Add: 3F, Gaotang Ind. Zone, Wenhu Rd, Liaobu, Shenzhen 518392 China
Tel: +86-139-4086 3827 Fax: +86-755-29483066
E-mail: morgan.pidd@brivexa-example.com

Font styles to use
Sans Serif
Other font styles liked:
• Tw Cen MT Condensed

Colors

Designer to choose only greyscale colors for use in the design.

Requirements
Must have
• Must have instructions of how to use the strip and CAUTION
• Must have CE, RoHS UL, trash can, ISO9001 logo
Nice to have
• Nice to have a back ground pictures with a strip drawing.

```html
<!DOCTYPE html>
<html lang="en">
<head>
<meta charset="utf-8">
<title>LED Strip – Brivexa Lighting Bag</title>
<link rel="stylesheet" href="https://fonts.googleapis.com/css2?family=Jost:wght@400&display=swap">
<style>
  :root {
    --silver-light: #d9d9d9;
    --silver-mid: #c9c9c9;
    --grey-lower: #b1b1b1;
    --grey-lower-deep: #a4a4a4;
    --pattern-dark: #2e2e2e;
    --pattern-light: #8a8a8a;
    --band-black: #1c1c1c;
    --branch-grey: #6f6f6f;
    --accent-orange: #e06a12;
    --ink-black: #1e1e1e;
  }
  html, body {
    margin: 0;
    padding: 0;
    width: 900px;
    height: 1200px;
    overflow: hidden;
    background: var(--silver-light);
  }
  .bag-face {
    position: relative;
    width: 900px;
    height: 1200px;
    overflow: hidden;
    font-family: "Jost", "Futura", sans-serif;
  }
  .upper-panel {
    position: absolute;
    left: 0; top: 0;
    width: 900px; height: 433px;
    background: linear-gradient(180deg, var(--silver-light) 0%, var(--silver-mid) 100%);
  }
  .geometric-band {
    position: absolute;
    left: 36px; top: 6px;
    width: 837px; height: 100px;
    background: linear-gradient(90deg, var(--pattern-dark), #4a4a4a 50%, var(--pattern-dark));
  }
  .zip-seal {
    position: absolute;
    left: 0; top: 128px;
    width: 900px; height: 6px;
    border-top: 1px solid #bdbdbd;
    border-bottom: 1px solid #ededed;
  }
  .blossom-band {
    position: absolute;
    left: 0; top: 433px;
    width: 900px; height: 354px;
    background: linear-gradient(100deg, var(--band-black) 0%, #3b3b3b 35%, var(--branch-grey) 55%, #2a2a2a 80%, var(--band-black) 100%);
  }
  .lower-panel {
    position: absolute;
    left: 0; top: 787px;
    width: 900px; height: 413px;
    background: linear-gradient(180deg, var(--grey-lower) 0%, var(--grey-lower-deep) 100%);
  }
  .wordmark {
    position: absolute;
    left: 0; top: 0;
    width: 900px; height: 1200px;
  }
  .wordmark text {
    font-family: "Jost", "Futura", sans-serif;
    font-weight: 400;
  }
  .wordmark .title-orange { fill: var(--accent-orange); }
  .wordmark .title-black { fill: var(--ink-black); }
</style>
</head>
<body>
  <main class="bag-face">
    <section class="upper-panel">
      <div class="geometric-band" role="img" aria-label="Black and white repeating diamond and chevron pattern band"></div>
      <div class="zip-seal"></div>
    </section>
    <section class="blossom-band" role="img" aria-label="Illustration of grey cherry blossom branches with white flowers and a small bird on a black background"></section>
    <section class="lower-panel"></section>

    <svg class="wordmark" viewBox="0 0 900 1200" xmlns="http://www.w3.org/2000/svg">
      <text class="title-orange" x="103" y="392" font-size="258" textLength="367" lengthAdjust="spacingAndGlyphs">LED</text>
      <text class="title-orange" x="515" y="320" font-size="142" textLength="310" lengthAdjust="spacingAndGlyphs">STRIP</text>
      <text class="title-black" x="99" y="1045" font-size="272" textLength="373" lengthAdjust="spacingAndGlyphs">LED</text>
      <text class="title-black" x="515" y="1045" font-size="142" textLength="310" lengthAdjust="spacingAndGlyphs">STRIP</text>
    </svg>
  </main>
</body>
</html>
```